New Business Card Options

we need a new business card design to reflect the edgy, innovative image we want the company to portray. We also need to include the social buttons to encourage more interaction with our social media accounts.
I've attached the current business card design which is a fold out card which has lines for writing notes on the back. I'm looking for options for design as well as printing suggestions - we want to stand out and be memorable.
THE BUSINESS CARD DOES NOT HAVE TO HAVE THE PHOTO
Colours to use:
MARINE
Dark blue R000 G031 B051
Light blue R080 G177 B234
Dark blue C100 M047 Y023 K079
Light blue C083 M001 Y000 K000
Reason: I just need an extra day to shortlist designs
Reason: need more time to decide
Target Market(s)
Marine
Industry/Entity Type
Business
Contact Information for Business Card
I've attached a copy of our current business card. the new business cards may or may not include the photo - i would like options of both. I would like our social media icons adding for Twitter, Linkedin, Facebook and YouTube
Font styles to use
Other font styles liked:
- Calibri
Look and feel
Each slider illustrates characteristics of the customer's brand and the style your logo design should communicate.

```html
<!DOCTYPE html>
<html lang="en">
<head>
<meta charset="utf-8">
<title>Keelwright Marine – Business Card</title>
<link rel="stylesheet" href="https://fonts.googleapis.com/css2?family=Quicksand:wght@500;700&display=swap">
<style>
  :root {
    --marine-dark: #001f33;
    --marine-light: #50b1ea;
    --stage: #e7e4e0;
    --frost-top: #eef0f2;
    --frost-mid: #dcdfe2;
    --frost-low: #e6d6da;
    --white: #ffffff;
  }
  html, body {
    margin: 0;
    padding: 0;
    width: 1200px;
    height: 970px;
    overflow: hidden;
    background: var(--stage);
  }
  .canvas {
    position: relative;
    width: 1200px;
    height: 970px;
  }
  .business-card {
    position: absolute;
    left: 80px;
    top: 196px;
    width: 1040px;
    height: 578px;
    display: flex;
    box-shadow: 0 10px 30px rgba(0, 0, 0, 0.18);
    font-family: "Quicksand", sans-serif;
  }
  .card-front-panel {
    position: relative;
    width: 489px;
    height: 100%;
    background: linear-gradient(180deg, var(--frost-top) 0%, var(--frost-mid) 55%, var(--frost-low) 80%, var(--frost-mid) 100%);
    border: 1px solid rgba(0, 0, 0, 0.25);
    border-right: none;
    box-sizing: border-box;
  }
  .brand-plate {
    position: absolute;
    left: 61px;
    top: 220px;
    width: 348px;
    height: 131px;
    background: var(--white);
    display: flex;
    align-items: center;
    justify-content: center;
  }
  .brand-name {
    font-weight: 700;
    font-size: 36px;
    color: var(--marine-dark);
    letter-spacing: 0.5px;
  }
  .contact-panel {
    position: relative;
    flex: 1;
    height: 100%;
    background: var(--marine-dark);
    color: var(--marine-light);
  }
  .panel-notch {
    position: absolute;
    left: -33px;
    top: 67px;
    width: 34px;
    height: 36px;
  }
  .address {
    position: absolute;
    left: 29px;
    top: 160px;
    margin: 0;
    font-size: 23px;
    font-weight: 500;
    line-height: 36px;
  }
  .contact-list {
    position: absolute;
    left: 29px;
    top: 250px;
    margin: 0;
    padding: 0;
    list-style: none;
  }
  .contact-item {
    display: flex;
    align-items: center;
    height: 45px;
    font-size: 23px;
    font-weight: 500;
  }
  .contact-icon {
    width: 20px;
    height: 20px;
    margin-right: 16px;
    flex: none;
  }
</style>
</head>
<body>
<div class="canvas">
  <div class="business-card">
    <div class="card-front-panel" role="img" aria-label="Frosted translucent card surface">
      <div class="brand-plate">
        <span class="brand-name">Keelwright Marine</span>
      </div>
    </div>
    <div class="contact-panel">
      <svg class="panel-notch" viewBox="0 0 34 36" aria-hidden="true">
        <polygon points="34,0 0,18 34,36" fill="var(--marine-dark)"/>
      </svg>
      <p class="address">Harbour Point, Westquay, Hullbridge<br>East Riding, HU9 4QT, UK</p>
      <ul class="contact-list">
        <li class="contact-item">
          <svg class="contact-icon" viewBox="0 0 20 20" aria-hidden="true">
            <rect x="5" y="1" width="10" height="18" rx="2" fill="none" stroke="var(--marine-light)" stroke-width="2"/>
            <rect x="8.5" y="15" width="3" height="1.6" fill="var(--marine-light)"/>
          </svg>
          +44 (0) 7700 900482
        </li>
        <li class="contact-item">
          <svg class="contact-icon" viewBox="0 0 20 20" aria-hidden="true">
            <circle cx="10" cy="10" r="8.5" fill="var(--marine-light)"/>
          </svg>
          sam.harlow27
        </li>
        <li class="contact-item">
          <svg class="contact-icon" viewBox="0 0 20 20" aria-hidden="true">
            <polygon points="1,9 19,2 13,18 9,11" fill="var(--marine-light)"/>
          </svg>
          sam.harlow@keelwright-marine.com
        </li>
        <li class="contact-item">
          <svg class="contact-icon" viewBox="0 0 20 20" aria-hidden="true">
            <circle cx="10" cy="10" r="8" fill="none" stroke="var(--marine-light)" stroke-width="2"/>
            <ellipse cx="10" cy="10" rx="3.5" ry="8" fill="none" stroke="var(--marine-light)" stroke-width="1.6"/>
            <line x1="2" y1="10" x2="18" y2="10" stroke="var(--marine-light)" stroke-width="1.6"/>
          </svg>
          www.keelwright-marine.com
        </li>
      </ul>
    </div>
  </div>
</div>
</body>
</html>
```